DominicRaleigh

I will be video blogging 1 - 5 minute instructional videos about all kind or stuff

I want it took look clean.
I have secured Dominicraleigh.com
Do you design youtube pages as well.
I will upload to youtube and correspond with websites.
Website wil include
videos with longer written description
how to book me.
where I am speaking at next
Thank you

Reason: my design is going to be more detailed than i had expected

Reason: still have changes

Youtube

```html
<!DOCTYPE html>
<html lang="en">
<head>
<meta charset="utf-8">
<title>Dominic Raleigh — Blog</title>
<link href="https://fonts.googleapis.com/css2?family=Open+Sans:wght@400;600;700&display=swap" rel="stylesheet">
<style>
:root{
  --ink:#1d1d1d;
  --body:#4a4a4a;
  --muted:#6d6d6d;
  --topbar:#241406;
  --header:#3a230d;
  --header-dark:#2c1907;
  --logo-box:#5b3b17;
  --accent:#3cb9ec;
  --accent-soft:#5cc8f2;
  --nav-active:#c9a06b;
  --brown:#6b3d0f;
  --brown-panel:#553614;
  --tab-active:#6e4c27;
  --btn-muted:#b9ab9b;
  --rule:#e4e4e4;
  --footer:#3b2108;
  --white:#ffffff;
}
*{box-sizing:border-box;margin:0;padding:0}
html,body{width:1200px;height:2531px;overflow:hidden}
body{font-family:"Open Sans",Arial,sans-serif;background:var(--white);color:var(--body);position:relative}

/* top news bar */
.news-bar{position:absolute;left:0;top:0;width:1200px;height:46px;background:var(--topbar);display:flex;align-items:center}
.news-label{position:relative;height:46px;display:flex;align-items:center;padding:0 22px 0 50px;background:#3a2410;color:var(--white);font-weight:700;font-size:15px;letter-spacing:.3px}
.news-label::after{content:"";position:absolute;right:-14px;top:0;border-left:14px solid #3a2410;border-top:23px solid transparent;border-bottom:23px solid transparent}
.news-text{margin-left:30px;color:#d9d2c8;font-size:14.5px}
.book-btn{position:absolute;left:990px;top:5px;width:194px;height:37px;background:var(--accent);color:var(--white);font-weight:700;font-size:15px;display:flex;align-items:center;justify-content:center;border-radius:2px;letter-spacing:.3px}

/* header */
.site-header{position:absolute;left:0;top:46px;width:1200px;height:85px;background:linear-gradient(var(--header),var(--header-dark))}
.brand{position:absolute;left:0;top:0;width:355px;height:85px;background:var(--logo-box);display:flex;align-items:center;padding-left:50px;color:var(--accent);font-size:36px;font-weight:400;letter-spacing:.5px}
.main-nav{position:absolute;top:0;height:85px;left:624px;display:flex;align-items:center}
.main-nav a{color:var(--white);text-decoration:none;font-size:17.5px;margin-right:33px}
.main-nav a.is-active{color:var(--nav-active)}
.main-nav a:last-child{margin-right:0}

/* posts */
.post{position:absolute;left:50px;width:659px;height:389px;border-bottom:1px solid var(--rule)}
.post-title{font-size:25.5px;font-weight:600;color:var(--ink);line-height:34px;white-space:nowrap}
.post-meta{margin-top:12px;height:20px;display:flex;align-items:center;font-size:13.5px;color:var(--muted)}
.post-meta span{display:flex;align-items:center;margin-right:20px}
.post-meta svg{margin-right:9px}
.post-body{position:absolute;top:93px;left:0;width:659px;height:232px}
.video{position:absolute;top:0;width:347px;height:232px;border:5px solid var(--accent);border-radius:4px;overflow:hidden}
.video .frame{position:absolute;inset:0}
.video .controls{position:absolute;left:0;right:0;bottom:0;height:16px;background:#1b1b1b}
.video .controls::before{content:"";position:absolute;left:30px;right:50px;top:7px;height:2px;background:#555}
.post-text{position:absolute;top:0;font-size:14.7px;line-height:22.2px;color:var(--body)}
.read-more{position:absolute;bottom:0;height:34px;width:91px;border-radius:4px;background:var(--btn-muted);color:var(--white);font-size:14px;display:flex;align-items:center;justify-content:center}
.read-more.is-primary{background:var(--brown)}
.post.video-left .video{left:0}
.post.video-left .post-text{left:376px;width:283px}
.post.video-left .read-more{left:376px}
.post.video-right .video{left:311px}
.post.video-right .post-text{left:0;width:290px}
.post.video-right .read-more{left:0}
.tone-a{background:radial-gradient(ellipse at 50% 45%,#6a4630,#2a1a10 70%)}
.tone-b{background:linear-gradient(180deg,#8a9096,#4a4f58 60%,#2f333c)}
.tone-c{background:linear-gradient(120deg,#3b4b5e,#8a97a6 55%,#c9cfd6)}

/* sidebar */
.sidebar{position:absolute;left:772px;top:0;width:378px}
.widget-title{position:absolute;left:0;font-size:24px;font-weight:400;color:var(--ink);letter-spacing:.2px}
.widget-title.is-accent{color:var(--accent)}
.about-photo{position:absolute;left:2px;top:224px;width:87px;height:92px;border:3px solid #e6e6e6;background:linear-gradient(#6e4a34,#2b1c14)}
.about-text{position:absolute;font-size:14.4px;line-height:21.5px;color:var(--body)}
.tabs{position:absolute;left:0;top:513px;width:378px;height:40px;background:var(--header-dark);border-radius:3px;display:flex;font-size:15px;color:var(--white)}
.tabs span{display:flex;align-items:center;justify-content:center}
.tabs .is-active{background:var(--tab-active);width:122px}
.tab-item{position:absolute;left:0;width:378px;height:122px;border-bottom:1px solid var(--rule)}
.tab-item .thumb{position:absolute;left:0;top:10px;width:86px;height:92px;border:3px solid #e8e8e8}
.tab-item h4{position:absolute;left:112px;top:10px;width:266px;font-size:13.5px;font-weight:400;color:var(--ink);line-height:20px}
.tab-item p{position:absolute;left:112px;top:52px;width:266px;font-size:12.8px;line-height:18px;color:var(--body)}
.speaking-video{position:absolute;left:2px;top:1127px;width:374px;height:219px;border:5px solid var(--accent);border-radius:4px;background:linear-gradient(100deg,#2f3a44,#6b7680 45%,#b9a796);overflow:hidden}
.play{position:absolute;left:160px;top:86px;width:50px;height:36px;background:#3a2410;border-radius:6px}
.play::after{content:"";position:absolute;left:20px;top:10px;border-left:14px solid var(--white);border-top:8px solid transparent;border-bottom:8px solid transparent}
.like-btn{position:absolute;left:2px;top:1428px;width:52px;height:21px;background:#4a66a0;color:var(--white);font-size:12px;font-weight:700;display:flex;align-items:center;justify-content:center;border-radius:2px}
.like-count{position:absolute;left:2px;top:1459px;font-size:12.5px;color:var(--body)}
.like-count b{font-weight:400;color:#3b5998}
.fan-grid{position:absolute;left:2px;top:1496px;width:374px;display:grid;grid-template-columns:repeat(5,68px);gap:8px 8px}
.fan-grid div{height:68px}
.plugin-note{position:absolute;left:2px;top:1655px;font-size:12.5px;color:var(--body);display:flex;align-items:center;border-top:1px solid var(--rule);padding-top:6px;width:374px}
.plugin-note i{display:inline-block;width:13px;height:13px;background:#4a66a0;margin-right:12px}
.subscribe{position:absolute;left:0;top:1757px;width:378px;height:121px;background:var(--brown-panel);border-radius:4px;padding:16px 0 0 16px;color:var(--white);font-size:12.4px;font-weight:600;line-height:17px;text-transform:uppercase}
.subscribe .field{position:absolute;left:16px;top:73px;width:232px;height:31px;background:var(--white);color:#777;font-weight:400;text-transform:none;font-size:13px;display:flex;align-items:center;padding-left:10px}
.subscribe .submit{position:absolute;left:264px;top:73px;width:92px;height:31px;background:var(--accent);display:flex;align-items:center;justify-content:center;font-size:13.5px;font-weight:700}
.recent{position:absolute;left:0;width:378px;height:84px}
.recent .thumb{position:absolute;left:2px;top:0;width:70px;height:70px;border:3px solid #e8e8e8;border-radius:4px}
.recent h4{position:absolute;left:92px;top:4px;width:286px;font-size:13.5px;font-weight:400;line-height:19px;color:var(--body)}
.recent .meta{position:absolute;left:92px;top:48px;display:flex;align-items:center;font-size:12.5px;color:var(--ink)}
.recent .meta svg{margin-right:8px}
.recent .meta .count{margin-right:14px}

/* footer */
.site-footer{position:absolute;left:0;top:2468px;width:1200px;height:63px;background:var(--footer);color:var(--white);font-size:14.5px;display:flex;align-items:center;justify-content:center}
</style>
</head>
<body>

<div class="news-bar">
  <div class="news-label">LATEST NEWS</div>
  <div class="news-text">Lorem Ipsum is simply dummy text of the printing and typesetting industry Lorem Ipsum</div>
  <div class="book-btn">HOW TO BOOK ME</div>
</div>

<header class="site-header">
  <div class="brand">DOMINIC RALEIGH</div>
  <nav class="main-nav">
    <a href="#">Home</a><a href="#">About Us</a><a href="#">Services</a><a href="#">Portfolio</a><a href="#" class="is-active">Blog</a><a href="#">Contact Us</a>
  </nav>
</header>

<main>
  <article class="post video-left" style="top:171px">
    <h2 class="post-title">This is Just Going to Be Another Test Post with Paragraphs</h2>
    <div class="post-meta">
      <span><svg width="14" height="14" viewBox="0 0 14 14"><rect x="1" y="2" width="12" height="11" fill="none" stroke="#7a5a30" stroke-width="1.5"/><rect x="1" y="2" width="12" height="3" fill="#7a5a30"/></svg>January 1.2014</span>
      <span><svg width="12" height="14" viewBox="0 0 12 14"><circle cx="6" cy="4" r="3" fill="#7a5a30"/><path d="M0 14c0-4 2.5-6 6-6s6 2 6 6z" fill="#7a5a30"/></svg>John Deo</span>
      <span><svg width="16" height="14" viewBox="0 0 16 14"><ellipse cx="8" cy="6" rx="7" ry="5" fill="none" stroke="#7a5a30" stroke-width="1.5"/><path d="M3 10l-1 4 4-3z" fill="#7a5a30"/></svg>2 Comments</span>
      <span><svg width="14" height="14" viewBox="0 0 14 14"><path d="M1 6h3v7H1zM5 6l3-5c1.5 0 2 1 1.5 2.5L9 5h4l-1.5 8H5z" fill="#7a5a30"/></svg>Share</span>
    </div>
    <div class="post-body">
      <div class="video"><div class="frame tone-a" role="img" aria-label="Video still of the speaker"></div><div class="controls"></div></div>
      <p class="post-text">Lorem Ipsum is simply dummy text of the printing and typesetting industry. Lorem Ipsum has bee the industry's standard dummy text ever since the 1500s, when an unknown printer took a galley of type and scrambled it to make a type specimen book. has survived not only five centuries, but also the leap into electronic typesetting, remaining</p>
      <div class="read-more is-primary">Read More</div>
    </div>
  </article>

  <article class="post video-right" style="top:560px">
    <h2 class="post-title">This is Just Going to Be Another Test Post with Paragraphs</h2>
    <div class="post-meta">
      <span><svg width="14" height="14" viewBox="0 0 14 14"><rect x="1" y="2" width="12" height="11" fill="none" stroke="#7a5a30" stroke-width="1.5"/><rect x="1" y="2" width="12" height="3" fill="#7a5a30"/></svg>January 1.2014</span>
      <span><svg width="12" height="14" viewBox="0 0 12 14"><circle cx="6" cy="4" r="3" fill="#7a5a30"/><path d="M0 14c0-4 2.5-6 6-6s6 2 6 6z" fill="#7a5a30"/></svg>John Deo</span>
      <span><svg width="16" height="14" viewBox="0 0 16 14"><ellipse cx="8" cy="6" rx="7" ry="5" fill="none" stroke="#7a5a30" stroke-width="1.5"/><path d="M3 10l-1 4 4-3z" fill="#7a5a30"/></svg>2 Comments</span>
      <span><svg width="14" height="14" viewBox="0 0 14 14"><path d="M1 6h3v7H1zM5 6l3-5c1.5 0 2 1 1.5 2.5L9 5h4l-1.5 8H5z" fill="#7a5a30"/></svg>Share</span>
    </div>
    <div class="post-body">
      <p class="post-text">Lorem Ipsum is simply dummy text of the printing and typesetting industry. Lorem Ipsum has bee the industry's standard dummy text ever since the 1500s, when an unknown printer took a galley of type and scrambled it to make a type specimen book. has survived not only five centuries, but also the leap into electronic typesetting, remaining</p>
      <div class="read-more">Read More</div>
      <div class="video"><div class="frame tone-b" role="img" aria-label="Video still of a presenter in a suit"></div><div class="controls"></div></div>
    </div>
  </article>

  <article class="post video-left" style="top:949px">
    <h2 class="post-title">This is Just Going to Be Another Test Post with Paragraphs</h2>
    <div class="post-meta">
      <span><svg width="14" height="14" viewBox="0 0 14 14"><rect x="1" y="2" width="12" height="11" fill="none" stroke="#7a5a30" stroke-width="1.5"/><rect x="1" y="2" width="12" height="3" fill="#7a5a30"/></svg>January 1.2014</span>
      <span><svg width="12" height="14" viewBox="0 0 12 14"><circle cx="6" cy="4" r="3" fill="#7a5a30"/><path d="M0 14c0-4 2.5-6 6-6s6 2 6 6z" fill="#7a5a30"/></svg>John Deo</span>
      <span><svg width="16" height="14" viewBox="0 0 16 14"><ellipse cx="8" cy="6" rx="7" ry="5" fill="none" stroke="#7a5a30" stroke-width="1.5"/><path d="M3 10l-1 4 4-3z" fill="#7a5a30"/></svg>2 Comments</span>
      <span><svg width="14" height="14" viewBox="0 0 14 14"><path d="M1 6h3v7H1zM5 6l3-5c1.5 0 2 1 1.5 2.5L9 5h4l-1.5 8H5z" fill="#7a5a30"/></svg>Share</span>
    </div>
    <div class="post-body">
      <div class="video"><div class="frame tone-a" role="img" aria-label="Video still of the speaker"></div><div class="controls"></div></div>
      <p class="post-text">Lorem Ipsum is simply dummy text of the printing and typesetting industry. Lorem Ipsum has bee the industry's standard dummy text ever since the 1500s, when an unknown printer took a galley of type and scrambled it to make a type specimen book. has survived not only five centuries, but also the leap into electronic typesetting, remaining</p>
      <div class="read-more">Read More</div>
    </div>
  </article>

  <article class="post video-right" style="top:1338px">
    <h2 class="post-title">This is Just Going to Be Another Test Post with Paragraphs</h2>
    <div class="post-meta">
      <span><svg width="14" height="14" viewBox="0 0 14 14"><rect x="1" y="2" width="12" height="11" fill="none" stroke="#7a5a30" stroke-width="1.5"/><rect x="1" y="2" width="12" height="3" fill="#7a5a30"/></svg>January 1.2014</span>
      <span><svg width="12" height="14" viewBox="0 0 12 14"><circle cx="6" cy="4" r="3" fill="#7a5a30"/><path d="M0 14c0-4 2.5-6 6-6s6 2 6 6z" fill="#7a5a30"/></svg>John Deo</span>
      <span><svg width="16" height="14" viewBox="0 0 16 14"><ellipse cx="8" cy="6" rx="7" ry="5" fill="none" stroke="#7a5a30" stroke-width="1.5"/><path d="M3 10l-1 4 4-3z" fill="#7a5a30"/></svg>2 Comments</span>
      <span><svg width="14" height="14" viewBox="0 0 14 14"><path d="M1 6h3v7H1zM5 6l3-5c1.5 0 2 1 1.5 2.5L9 5h4l-1.5 8H5z" fill="#7a5a30"/></svg>Share</span>
    </div>
    <div class="post-body">
      <p class="post-text">Lorem Ipsum is simply dummy text of the printing and typesetting industry. Lorem Ipsum has bee the industry's standard dummy text ever since the 1500s, when an unknown printer took a galley of type and scrambled it to make a type specimen book. has survived not only five centuries, but also the leap into electronic typesetting, remaining</p>
      <div class="read-more">Read More</div>
      <div class="video"><div class="frame tone-b" role="img" aria-label="Video still of a presenter in a suit"></div><div class="controls"></div></div>
    </div>
  </article>

  <article class="post video-left" style="top:1727px">
    <h2 class="post-title">This is Just Going to Be Another Test Post with Paragraphs</h2>
    <div class="post-meta">
      <span><svg width="14" height="14" viewBox="0 0 14 14"><rect x="1" y="2" width="12" height="11" fill="none" stroke="#7a5a30" stroke-width="1.5"/><rect x="1" y="2" width="12" height="3" fill="#7a5a30"/></svg>January 1.2014</span>
      <span><svg width="12" height="14" viewBox="0 0 12 14"><circle cx="6" cy="4" r="3" fill="#7a5a30"/><path d="M0 14c0-4 2.5-6 6-6s6 2 6 6z" fill="#7a5a30"/></svg>John Deo</span>
      <span><svg width="16" height="14" viewBox="0 0 16 14"><ellipse cx="8" cy="6" rx="7" ry="5" fill="none" stroke="#7a5a30" stroke-width="1.5"/><path d="M3 10l-1 4 4-3z" fill="#7a5a30"/></svg>2 Comments</span>
      <span><svg width="14" height="14" viewBox="0 0 14 14"><path d="M1 6h3v7H1zM5 6l3-5c1.5 0 2 1 1.5 2.5L9 5h4l-1.5 8H5z" fill="#7a5a30"/></svg>Share</span>
    </div>
    <div class="post-body">
      <div class="video"><div class="frame tone-c" role="img" aria-label="Video still of business people in an office"></div><div class="controls"></div></div>
      <p class="post-text">Lorem Ipsum is simply dummy text of the printing and typesetting industry. Lorem Ipsum has bee the industry's standard dummy text ever since the 1500s, when an unknown printer took a galley of type and scrambled it to make a type specimen book. has survived not only five centuries, but also the leap into electronic typesetting, remaining</p>
      <div class="read-more">Read More</div>
    </div>
  </article>

  <article class="post video-right" style="top:2116px;border-bottom:none">
    <h2 class="post-title">This is Just Going to Be Another Test Post with Paragraphs</h2>
    <div class="post-meta">
      <span><svg width="14" height="14" viewBox="0 0 14 14"><rect x="1" y="2" width="12" height="11" fill="none" stroke="#7a5a30" stroke-width="1.5"/><rect x="1" y="2" width="12" height="3" fill="#7a5a30"/></svg>January 1.2014</span>
      <span><svg width="12" height="14" viewBox="0 0 12 14"><circle cx="6" cy="4" r="3" fill="#7a5a30"/><path d="M0 14c0-4 2.5-6 6-6s6 2 6 6z" fill="#7a5a30"/></svg>John Deo</span>
      <span><svg width="16" height="14" viewBox="0 0 16 14"><ellipse cx="8" cy="6" rx="7" ry="5" fill="none" stroke="#7a5a30" stroke-width="1.5"/><path d="M3 10l-1 4 4-3z" fill="#7a5a30"/></svg>2 Comments</span>
      <span><svg width="14" height="14" viewBox="0 0 14 14"><path d="M1 6h3v7H1zM5 6l3-5c1.5 0 2 1 1.5 2.5L9 5h4l-1.5 8H5z" fill="#7a5a30"/></svg>Share</span>
    </div>
    <div class="post-body">
      <p class="post-text">Lorem Ipsum is simply dummy text of the printing and typesetting industry. Lorem Ipsum has bee the industry's standard dummy text ever since the 1500s, when an unknown printer took a galley of type and scrambled it to make a type specimen book. has survived not only five centuries, but also the leap into electronic typesetting, remaining</p>
      <div class="read-more">Read More</div>
      <div class="video"><div class="frame tone-b" role="img" aria-label="Video still of a presenter in a suit"></div><div class="controls"></div></div>
    </div>
  </article>
</main>

<aside class="sidebar">
  <h3 class="widget-title" style="top:163px">ABOUT US</h3>
  <div class="about-photo" role="img" aria-label="Portrait of Dominic Raleigh"></div>
  <p class="about-text" style="left:123px;top:218px;width:255px">Lorem Ipsum is simply dummy text of the printing and typesetting industry. Lorem Ipsum has been the industry's standard dummy text ever since the 1500s, when</p>
  <p class="about-text" style="left:0;top:326px;width:378px">Lorem Ipsum is simply dummy text of the printing and typesetting industry. Lorem Ipsum has been the industry's standard dummy text ever since the 1500s, when an unknown printer took a galley of type and scrambled it to make a type specimen book.</p>
  <div class="read-more" style="left:0;top:449px">Read More</div>

  <div class="tabs"><span class="is-active">POPULAR</span><span style="width:112px">VIDEO</span><span style="width:144px">CATEGORY</span></div>

  <div class="tab-item" style="top:556px">
    <div class="thumb" role="img" aria-label="Photo of a person on a mountain at sunrise" style="background:linear-gradient(#c9d6e4,#7a8a98)"></div>
    <h4>This is Just Going to Be Another Test Post with Paragraphs</h4>
    <p>Lorem ipsum no has veniam elaboraret con-stituam, ne nibh posidonium vel. Has ad quaeque omittantur, malis abhorreant eam</p>
  </div>
  <div class="tab-item" style="top:678px">
    <div class="thumb" role="img" aria-label="Photo of a woman outdoors" style="background:linear-gradient(#8cc0d8,#c9a27a)"></div>
    <h4>This is Just Going to Be Another Test Post with Paragraphs</h4>
    <p>Lorem ipsum no has veniam elaboraret con-stituam, ne nibh posidonium vel. Has ad quaeque omittantur, malis abhorreant eam</p>
  </div>
  <div class="tab-item" style="top:800px">
    <div class="thumb" role="img" aria-label="Photo of a climber on a summit" style="background:linear-gradient(#7fa6c9,#5a4a3a)"></div>
    <h4>This is Just Going to Be Another Test Post with Paragraphs</h4>
    <p>Lorem ipsum no has veniam elaboraret con-stituam, ne nibh posidonium vel. Has ad quaeque omittantur, malis abhorreant eam</p>
  </div>
  <div class="tab-item" style="top:922px;border-bottom:none">
    <div class="thumb" role="img" aria-label="Photo of a person jumping between rocks" style="background:linear-gradient(#9cc3e2,#8a7a68)"></div>
    <h4>This is Just Going to Be Another Test Post with Paragraphs</h4>
    <p>Lorem ipsum no has veniam elaboraret constituam, ne nibh posidonium vel. Has ad quaeque omittantur, malis abhorreant eam</p>
  </div>

  <h3 class="widget-title is-accent" style="top:1080px">WHERE I AM SPEAKING</h3>
  <div class="speaking-video" role="img" aria-label="Video still of a speaker at an event"><div class="play"></div></div>

  <h3 class="widget-title" style="top:1382px">FIND US ON CIRCLEBOOK</h3>
  <div class="like-btn">Like</div>
  <div class="like-count">32,999 People like <b>circlebook</b></div>
  <div class="fan-grid" role="img" aria-label="Grid of follower profile photos">
    <div style="background:#d8c2a8"></div><div style="background:#b88a6a"></div><div style="background:#8a6a55"></div><div style="background:#c9b49a"></div><div style="background:#a67b5c"></div>
    <div style="background:#b58f72"></div><div style="background:#cdb8a0"></div><div style="background:#7a5a48"></div><div style="background:#d4a57a"></div><div style="background:#9c7860"></div>
  </div>
  <div class="plugin-note"><i></i>Circlebook Social Plugin</div>

  <h3 class="widget-title" style="top:1704px">FOLLOW BY EMAIL</h3>
  <div class="subscribe">Join with thousands of subscribe!<br>Get our latest articals delivered<br>to your email inbox
    <div class="field">Email address</div>
    <div class="submit">SUBMIT</div>
  </div>

  <h3 class="widget-title" style="top:1909px">RECENT POST</h3>
  <div class="recent" style="top:1962px">
    <div class="thumb" role="img" aria-label="Portrait photo" style="background:linear-gradient(#e8d6c0,#c49a78)"></div>
    <h4>This is Just Going to Be Another Test Post with Paragraphs</h4>
    <div class="meta"><svg width="16" height="14" viewBox="0 0 16 14"><ellipse cx="8" cy="6" rx="7" ry="5" fill="none" stroke="#7a5a30" stroke-width="1.5"/><path d="M3 10l-1 4 4-3z" fill="#7a5a30"/></svg><span class="count">3</span><svg width="14" height="14" viewBox="0 0 14 14"><rect x="1" y="2" width="12" height="11" fill="none" stroke="#7a5a30" stroke-width="1.5"/><rect x="1" y="2" width="12" height="3" fill="#7a5a30"/></svg>21 NOV 2014</div>
  </div>
  <div class="recent" style="top:2046px">
    <div class="thumb" role="img" aria-label="Portrait photo" style="background:linear-gradient(#c44a3a,#e0c0a0)"></div>
    <h4>This is Just Going to Be Another Test Post with Paragraphs</h4>
    <div class="meta"><svg width="16" height="14" viewBox="0 0 16 14"><ellipse cx="8" cy="6" rx="7" ry="5" fill="none" stroke="#7a5a30" stroke-width="1.5"/><path d="M3 10l-1 4 4-3z" fill="#7a5a30"/></svg><span class="count">3</span><svg width="14" height="14" viewBox="0 0 14 14"><rect x="1" y="2" width="12" height="11" fill="none" stroke="#7a5a30" stroke-width="1.5"/><rect x="1" y="2" width="12" height="3" fill="#7a5a30"/></svg>21 NOV 2014</div>
  </div>
  <div class="recent" style="top:2130px">
    <div class="thumb" role="img" aria-label="Portrait photo" style="background:linear-gradient(#7aa45a,#b08a68)"></div>
    <h4>This is Just Going to Be Another Test Post with Paragraphs</h4>
    <div class="meta"><svg width="16" height="14" viewBox="0 0 16 14"><ellipse cx="8" cy="6" rx="7" ry="5" fill="none" stroke="#7a5a30" stroke-width="1.5"/><path d="M3 10l-1 4 4-3z" fill="#7a5a30"/></svg><span class="count">3</span><svg width="14" height="14" viewBox="0 0 14 14"><rect x="1" y="2" width="12" height="11" fill="none" stroke="#7a5a30" stroke-width="1.5"/><rect x="1" y="2" width="12" height="3" fill="#7a5a30"/></svg>21 NOV 2014</div>
  </div>
  <div class="recent" style="top:2214px">
    <div class="thumb" role="img" aria-label="Portrait photo" style="background:linear-gradient(#d8b89a,#8a5a48)"></div>
    <h4>This is Just Going to Be Another Test Post with Paragraphs</h4>
    <div class="meta"><svg width="16" height="14" viewBox="0 0 16 14"><ellipse cx="8" cy="6" rx="7" ry="5" fill="none" stroke="#7a5a30" stroke-width="1.5"/><path d="M3 10l-1 4 4-3z" fill="#7a5a30"/></svg><span class="count">3</span><svg width="14" height="14" viewBox="0 0 14 14"><rect x="1" y="2" width="12" height="11" fill="none" stroke="#7a5a30" stroke-width="1.5"/><rect x="1" y="2" width="12" height="3" fill="#7a5a30"/></svg>21 NOV 2014</div>
  </div>
  <div class="recent" style="top:2298px">
    <div class="thumb" role="img" aria-label="Portrait photo" style="background:linear-gradient(#e4cdb0,#a8845e)"></div>
    <h4>This is Just Going to Be Another Test Post with Paragraphs</h4>
    <div class="meta"><svg width="16" height="14" viewBox="0 0 16 14"><ellipse cx="8" cy="6" rx="7" ry="5" fill="none" stroke="#7a5a30" stroke-width="1.5"/><path d="M3 10l-1 4 4-3z" fill="#7a5a30"/></svg><span class="count">3</span><svg width="14" height="14" viewBox="0 0 14 14"><rect x="1" y="2" width="12" height="11" fill="none" stroke="#7a5a30" stroke-width="1.5"/><rect x="1" y="2" width="12" height="3" fill="#7a5a30"/></svg>21 NOV 2014</div>
  </div>
</aside>

<footer class="site-footer">Copyright © 2014 All Right Reserved</footer>

</body>
</html>
```